A private security company called "Tavrin Security Services Ltd"

Hello everybody,

We need a web page for a company based in NZ. It is mainly an informative website so it would be wonderful if the designer puts their absolute best into making it a website that I would really appreciate. The website needs to show professionalism and also needs to make our web surfers find the information they need in a click. the company's colour is black and silver, and if those two colours could be integrated into the website it would be absolutely lovely. Please do contact me for any information.

Sincerely,
Dorian Velasko

Industry/Entity Type

Security

```html
<!DOCTYPE html>
<html lang="en">
<head>
<meta charset="utf-8">
<title>Our Security Solutions – Tavrin Security Services Ltd</title>
<link href="https://fonts.googleapis.com/css2?family=Oswald:wght@300;400&family=Arimo:wght@400;700&display=swap" rel="stylesheet">
<style>
  :root {
    --header-top: #fafafa;
    --header-bottom: #dcdcdc;
    --banner-top: #4a4a4a;
    --banner-bottom: #1c1c1c;
    --ink: #111111;
    --body-text: #6a6a6a;
    --nav-text: #2a2a2a;
    --frame: #e6e6e6;
    --silver: #b9b9b9;
    --divider: #e4e4e4;
    --footer-top: #3a3a3a;
    --footer-bottom: #262626;
    --footer-text: #8e8e8e;
    --footer-heading: #e8e8e8;
    --white: #ffffff;
  }
  * { margin: 0; padding: 0; box-sizing: border-box; }
  html, body { width: 1200px; height: 2779px; overflow: hidden; }
  body { position: relative; background: var(--white); font-family: "Arimo", Arial, sans-serif; }

  /* Header */
  .site-header {
    position: absolute; top: 0; left: 0; width: 1200px; height: 160px;
    background: linear-gradient(var(--header-top), var(--header-bottom));
    border-bottom: 1px solid #c8c8c8;
  }
  .brand { position: absolute; left: 152px; top: 54px; display: flex; align-items: center; gap: 10px; }
  .brand-mark { width: 22px; height: 22px; background: var(--ink); }
  .brand-name {
    font-family: "Oswald", sans-serif; font-weight: 400; font-size: 17px; color: var(--ink);
    line-height: 1.2; width: 170px; text-transform: uppercase;
  }
  .tagline {
    position: absolute; left: 418px; top: 26px;
    font-family: "Oswald", sans-serif; font-weight: 400; font-size: 24px; color: var(--ink); letter-spacing: 0.5px;
  }
  .main-nav { position: absolute; left: 416px; top: 100px; display: flex; gap: 30px; }
  .main-nav a {
    font-size: 13px; color: var(--nav-text); text-decoration: none; text-transform: uppercase; position: relative;
  }
  .main-nav a.is-active::after {
    content: ""; position: absolute; left: -2px; right: -2px; top: 43px; height: 3px; background: var(--silver);
  }
  .nav-pointer { position: absolute; left: 658px; top: 134px; }
  .social { position: absolute; display: flex; gap: 10px; }
  .social span { width: 30px; height: 30px; border-radius: 50%; background: var(--silver); display: block; }
  .social-header { left: 936px; top: 31px; }

  /* Banner */
  .page-banner {
    position: absolute; top: 160px; left: 0; width: 1200px; height: 162px;
    background: linear-gradient(var(--banner-top), var(--banner-bottom));
  }
  .page-title {
    position: absolute; left: 194px; top: 62px;
    font-family: "Oswald", sans-serif; font-weight: 400; font-size: 24px; color: var(--white); text-transform: uppercase;
  }
  .banner-visual {
    position: absolute; left: 850px; top: 12px; width: 190px; height: 130px; border-radius: 60px 20px 30px 40px;
    background: radial-gradient(circle at 40% 50%, #d8d8d8, #6a6a6a 60%, #2a2a2a);
  }

  /* Services */
  .service { position: absolute; left: 0; width: 1200px; height: 216px; }
  .service-photo {
    position: absolute; top: 0; width: 370px; height: 216px; background: var(--frame); padding: 10px;
  }
  .service-photo .fill { width: 100%; height: 100%; }
  .service-text { position: absolute; top: 0; width: 490px; }
  .service--photo-left .service-photo { left: 158px; }
  .service--photo-left .service-text { left: 558px; }
  .service--photo-right .service-photo { left: 676px; }
  .service--photo-right .service-text { left: 158px; }
  .service-title {
    font-family: "Oswald", sans-serif; font-weight: 400; font-size: 21px; color: var(--ink); margin-bottom: 14px; line-height: 1.2;
  }
  .service-text p { font-size: 11px; line-height: 15.4px; color: var(--body-text); margin-bottom: 15px; }
  .divider {
    position: absolute; left: 330px; width: 540px; height: 1px;
    background: linear-gradient(90deg, transparent, var(--divider), transparent);
  }

  /* Footer */
  .site-footer {
    position: absolute; top: 2310px; left: 0; width: 1200px; height: 469px;
    background: linear-gradient(var(--footer-top), var(--footer-bottom));
  }
  .footer-heading {
    font-family: "Oswald", sans-serif; font-weight: 300; font-size: 28px; color: var(--footer-heading); margin-bottom: 20px;
  }
  .footer-col { position: absolute; top: 68px; }
  .footer-about { left: 158px; width: 305px; }
  .footer-about p { font-size: 11px; line-height: 15.4px; color: var(--footer-text); margin-bottom: 15px; }
  .footer-links { left: 540px; width: 190px; }
  .footer-links ul { list-style: none; }
  .footer-links li {
    position: relative; padding-left: 24px; font-size: 12px; line-height: 15px; color: var(--footer-text);
    text-transform: uppercase; margin-bottom: 17px;
  }
  .footer-links li svg { position: absolute; left: 0; top: 2px; }
  .footer-contact { left: 768px; width: 300px; }
  .company-label { font-size: 12px; font-weight: 700; color: var(--footer-text); text-transform: uppercase; margin-bottom: 22px; }
  .contact-row { display: flex; gap: 14px; font-size: 12px; line-height: 15px; color: var(--footer-text); margin-bottom: 14px; }
  .contact-row svg { flex: none; }
  .contact-row span { text-transform: uppercase; }
  .contact-row .email { text-transform: none; }
  .footer-rule { position: absolute; left: 0; top: 390px; width: 1200px; height: 1px; background: #444; }
  .copyright { position: absolute; left: 158px; top: 424px; font-size: 12px; color: var(--footer-text); }
  .social-footer { left: 936px; top: 414px; }
  .social-footer span { background: #8a8a8a; }
</style>
</head>
<body>

<header class="site-header">
  <div class="brand">
    <span class="brand-mark"></span>
    <span class="brand-name">Tavrin Security Services Ltd.</span>
  </div>
  <div class="tagline">Vigilance You Can Rely On</div>
  <nav class="main-nav">
    <a href="#">Home</a>
    <a href="#">About Us</a>
    <a href="#" class="is-active">Our Security Solutions</a>
    <a href="#">Industries We Serve</a>
    <a href="#">Contact Us</a>
  </nav>
  <svg class="nav-pointer" width="14" height="10" viewBox="0 0 14 10"><path d="M0 10 L7 0 L14 10Z" fill="#b9b9b9"/></svg>
  <div class="social social-header"><span></span><span></span><span></span></div>
</header>

<section class="page-banner">
  <h1 class="page-title">Our Security Solutions</h1>
  <div class="banner-visual" role="img" aria-label="Photo of a security surveillance camera"></div>
</section>

<main>
  <article class="service service--photo-left" style="top:386px">
    <div class="service-photo"><div class="fill" role="img" aria-label="Photo of hands holding a small model house" style="background:linear-gradient(135deg,#e8e2dc,#c8836a 55%,#d9cfc6)"></div></div>
    <div class="service-text">
      <h2 class="service-title">Property Guards</h2>
      <p>Lorem ipsum dolor sit amet, consectetur adipiscing elit. In ut iaculis enim. Ut cursus est diam, eget semper erat auctor nec. Nullam vulputate est convallis, sollicitudin lib ero et, ornare lectus. Donec sagittis metus elit, et accumsan nisi porta non.</p>
      <p>Sed in tortor odio. Ut vulputate arcu neque, eu gravida tortor volutpat quis. Aliquam aliquam, eros in viverra accumsan, nibh turpis fermentum lacus, at dignissim tortor lectus vel mauris. Maecenas posuere bibendum augue, sit amet suscipit felis interd um ut. Fusce euismod erat non dictum pharetra. Aliquam sodales, orci non pulvinar consequat, lectus ante sollicitudin metus, posuere varius dolor nisi eget lacus. Donec gravida ullamcorper quam ultrices lobortis. In fermentum elementum scelerisque. Pellentesque habitant morbi tristique senectus et netus et</p>
    </div>
  </article>
  <div class="divider" style="top:660px"></div>

  <article class="service service--photo-right" style="top:710px">
    <div class="service-text">
      <h2 class="service-title">Personal Bodyguards</h2>
      <p>Lorem ipsum dolor sit amet, consectetur adipiscing elit. In ut iaculis enim. Ut cursus est diam, eget semper erat auctor nec. Nullam vulputate est convallis, sollicitudin lib ero et, ornare lectus. Donec sagittis metus elit, et accumsan nisi porta non.</p>
      <p>Sed in tortor odio. Ut vulputate arcu neque, eu gravida tortor volutpat quis. Aliquam aliquam, eros in viverra accumsan, nibh turpis fermentum lacus, at dignissim tortor lectus vel mauris. Maecenas posuere bibendum augue, sit amet suscipit felis interd um ut. Fusce euismod erat non dictum pharetra. Aliquam sodales, orci non pulvinar consequat, lectus ante sollicitudin metus, posuere varius dolor nisi eget lacus. Donec gravida ullamcorper quam ultrices lobortis. In fermentum elementum scelerisque. Pellentesque habitant morbi tristique senectus et netus et</p>
    </div>
    <div class="service-photo"><div class="fill" role="img" aria-label="Photo of a bodyguard with folded arms in a dark shirt" style="background:radial-gradient(circle at 50% 50%,#3a3a3a,#0c0c0c 70%)"></div></div>
  </article>
  <div class="divider" style="top:984px"></div>

  <article class="service service--photo-left" style="top:1034px">
    <div class="service-photo"><div class="fill" role="img" aria-label="Photo of an investigator photographing from a car window" style="background:linear-gradient(90deg,#1e1e1e 30%,#8a8f93 60%,#c9ccce)"></div></div>
    <div class="service-text">
      <h2 class="service-title">Private Investigation</h2>
      <p>Lorem ipsum dolor sit amet, consectetur adipiscing elit. In ut iaculis enim. Ut cursus est diam, eget semper erat auctor nec. Nullam vulputate est convallis, sollicitudin lib ero et, ornare lectus. Donec sagittis metus elit, et accumsan nisi porta non.</p>
      <p>Sed in tortor odio. Ut vulputate arcu neque, eu gravida tortor volutpat quis. Aliquam aliquam, eros in viverra accumsan, nibh turpis fermentum lacus, at dignissim tortor lectus vel mauris. Maecenas posuere bibendum augue, sit amet suscipit felis interd um ut. Fusce euismod erat non dictum pharetra. Aliquam sodales, orci non pulvinar consequat, lectus ante sollicitudin metus, posuere varius dolor nisi eget lacus. Donec gravida ullamcorper quam ultrices lobortis. In fermentum elementum scelerisque. Pellentesque habitant morbi tristique senectus et netus et</p>
    </div>
  </article>
  <div class="divider" style="top:1308px"></div>

  <article class="service service--photo-right" style="top:1358px">
    <div class="service-text">
      <h2 class="service-title">Corporate Event Security</h2>
      <p>Lorem ipsum dolor sit amet, consectetur adipiscing elit. In ut iaculis enim. Ut cursus est diam, eget semper erat auctor nec. Nullam vulputate est convallis, sollicitudin lib ero et, ornare lectus. Donec sagittis metus elit, et accumsan nisi porta non.</p>
      <p>Sed in tortor odio. Ut vulputate arcu neque, eu gravida tortor volutpat quis. Aliquam aliquam, eros in viverra accumsan, nibh turpis fermentum lacus, at dignissim tortor lectus vel mauris. Maecenas posuere bibendum augue, sit amet suscipit felis interd um ut. Fusce euismod erat non dictum pharetra. Aliquam sodales, orci non pulvinar consequat, lectus ante sollicitudin metus, posuere varius dolor nisi eget lacus. Donec gravida ullamcorper quam ultrices lobortis. In fermentum elementum scelerisque. Pellentesque habitant morbi tristique senectus et netus et</p>
    </div>
    <div class="service-photo"><div class="fill" role="img" aria-label="Photo of security staff at an outdoor event" style="background:linear-gradient(180deg,#6f8a4e,#a8a08e 40%,#151515 65%)"></div></div>
  </article>
  <div class="divider" style="top:1632px"></div>

  <article class="service service--photo-left" style="top:1682px">
    <div class="service-photo"><div class="fill" role="img" aria-label="Photo of two businessmen shaking hands seen from above" style="background:linear-gradient(135deg,#9aa0a3,#2a2a2a 50%,#b7b9ba)"></div></div>
    <div class="service-text">
      <h2 class="service-title">Security Consultancy</h2>
      <p>Lorem ipsum dolor sit amet, consectetur adipiscing elit. In ut iaculis enim. Ut cursus est diam, eget semper erat auctor nec. Nullam vulputate est convallis, sollicitudin lib ero et, ornare lectus. Donec sagittis metus elit, et accumsan nisi porta non.</p>
      <p>Sed in tortor odio. Ut vulputate arcu neque, eu gravida tortor volutpat quis. Aliquam aliquam, eros in viverra accumsan, nibh turpis fermentum lacus, at dignissim tortor lectus vel mauris. Maecenas posuere bibendum augue, sit amet suscipit felis interd um ut. Fusce euismod erat non dictum pharetra. Aliquam sodales, orci non pulvinar consequat, lectus ante sollicitudin metus, posuere varius dolor nisi eget lacus. Donec gravida ullamcorper quam ultrices lobortis. In fermentum elementum scelerisque. Pellentesque habitant morbi tristique senectus et netus et</p>
    </div>
  </article>
  <div class="divider" style="top:1956px"></div>

  <article class="service service--photo-right" style="top:2006px">
    <div class="service-text">
      <h2 class="service-title">Excutive Protection</h2>
      <p>Lorem ipsum dolor sit amet, consectetur adipiscing elit. In ut iaculis enim. Ut cursus est diam, eget semper erat auctor nec. Nullam vulputate est convallis, sollicitudin lib ero et, ornare lectus. Donec sagittis metus elit, et accumsan nisi porta non.</p>
      <p>Sed in tortor odio. Ut vulputate arcu neque, eu gravida tortor volutpat quis. Aliquam aliquam, eros in viverra accumsan, nibh turpis fermentum lacus, at dignissim tortor lectus vel mauris. Maecenas posuere bibendum augue, sit amet suscipit felis interd um ut. Fusce euismod erat non dictum pharetra. Aliquam sodales, orci non pulvinar consequat, lectus ante sollicitudin metus, posuere varius dolor nisi eget lacus. Donec gravida ullamcorper quam ultrices lobortis. In fermentum elementum scelerisque. Pellentesque habitant morbi tristique senectus et netus et</p>
    </div>
    <div class="service-photo"><div class="fill" role="img" aria-label="Photo of protection agents beside a black SUV" style="background:linear-gradient(180deg,#7e8a96,#1a1a1a 45%,#3b3b3b 80%,#8d8d8d)"></div></div>
  </article>
</main>

<footer class="site-footer">
  <div class="footer-col footer-about">
    <h3 class="footer-heading">About us</h3>
    <p>Lorem ipsum dolor sit amet, consectetur adipiscing elit. Morbi pellentesque iaculis justo eget fermentum. Pellentesque commodo iaculis neque, vitae tincidun odio pellentesque luctus. Aenean in eros eu magna vestibulum imperdiet pretium nec augue.</p>
    <p>Etiam quis turpis enim. Vestibulum auctor id mauris vulputate consequat. Suspendisse potenti. Cras at imperdiet elit. Integer fringilla tellus non diam condimentum, sed ultricies urna ultricies. Sed cong dui quis dui convallis dictum. Donec malesuada vulputate risus vitae bibendum. Maecenas in congue urna. Sed porttitor bibendum.</p>
  </div>
  <div class="footer-col footer-links">
    <h3 class="footer-heading">Quick Links</h3>
    <ul>
      <li><svg width="8" height="10" viewBox="0 0 8 10"><path d="M1 1 L6 5 L1 9" stroke="#ddd" stroke-width="2" fill="none"/></svg>Home</li>
      <li><svg width="8" height="10" viewBox="0 0 8 10"><path d="M1 1 L6 5 L1 9" stroke="#ddd" stroke-width="2" fill="none"/></svg>About Us</li>
      <li><svg width="8" height="10" viewBox="0 0 8 10"><path d="M1 1 L6 5 L1 9" stroke="#ddd" stroke-width="2" fill="none"/></svg>Our Security<br>Solutions</li>
      <li><svg width="8" height="10" viewBox="0 0 8 10"><path d="M1 1 L6 5 L1 9" stroke="#ddd" stroke-width="2" fill="none"/></svg>Industries We<br>Serve</li>
      <li><svg width="8" height="10" viewBox="0 0 8 10"><path d="M1 1 L6 5 L1 9" stroke="#ddd" stroke-width="2" fill="none"/></svg>Contact Us</li>
    </ul>
  </div>
  <div class="footer-col footer-contact">
    <h3 class="footer-heading">Contact Us</h3>
    <div class="company-label">Tavrin Security Services Ltd.</div>
    <div class="contact-row">
      <svg width="16" height="18" viewBox="0 0 16 18"><path d="M8 0a6 6 0 0 0-6 6c0 4.5 6 12 6 12s6-7.5 6-12a6 6 0 0 0-6-6z" fill="#e6e6e6"/><circle cx="8" cy="6" r="2.3" fill="#303030"/></svg>
      <span>12 Harrow Lane, Kelmont,<br>Waikato 3204, New Zealand</span>
    </div>
    <div class="contact-row">
      <svg width="16" height="16" viewBox="0 0 16 16"><path d="M3 1 L6 1 L7 5 L5 6.5 Q6.5 9.5 9.5 11 L11 9 L15 10 L15 13 Q15 15 13 15 Q1 14 1 3 Q1 1 3 1Z" fill="#e6e6e6"/></svg>
      <span>+64 7 555 0148</span>
    </div>
    <div class="contact-row">
      <svg width="16" height="12" viewBox="0 0 16 12"><rect x="0" y="0" width="16" height="12" rx="1" fill="#e6e6e6"/><path d="M1 1 L8 7 L15 1" stroke="#303030" stroke-width="1.3" fill="none"/></svg>
      <span class="email">info@tavrinsecurityservices.com</span>
    </div>
  </div>
  <div class="footer-rule"></div>
  <div class="copyright">Copyright © 2014 Tavrin Security Service LTD.</div>
  <div class="social social-footer"><span></span><span></span><span></span></div>
</footer>

</body>
</html>
```